Wendrows Accountants and Tax Agents Practice

We need an update on our logo.
We require Letterhead, withcomp slips, and business cards for three partners
We currently have a logo and which is used on our letterheads but we need a much more professional and updated more modern version.
We are an Accounting Practice which needs upating. I will up load what we currently use and please use the all the wording and what another designer has proposed but need it to be different .
The colour scheme needs to be deep charcoal and a deep blue/green(065A7F) .

Target Market(s)

Individuals, companies, partnerships

Industry/Entity Type

Accounting

Font styles to use
Other font styles liked:
• ITC Avant Garde Gothic.

Colors
0393ce

Requirements
Must have
• Please follow the letter head upload the colour code and the colour charcoal.
• I would like the word Wendrows in bold Accountants (not bold) the font to be ITC Avant Garde Gothic.
• The business cards for all three partners need to have two sides the solid colour on one side with the name Wendrows Accountants. The other side with the name and details ( below details for each partner) Dorian Fellbracke FCPA, Gerald Trumbleton FCPA
• Martin Osgood (Blue/green) the T, F, E, W ( blue green) the rest in charcoal with white background
• FCPA
• 2718 Park Road Ashvale VIC 3199
• T +61 3 94827713
• F + 61 9482 7159
• E martin@wendrows-example.com.au
• W wendrowsaccountants-example.com.au
• the letter faded letter G on the white side of the card in the top RH corner
Nice to have
• the letter G on the white side of the business card in shades of charcoal very faint
• Instead of E: for email using symbols for the details eg:✉

```html
<!DOCTYPE html>
<html lang="en">
<head>
<meta charset="utf-8">
<title>Wendrows Accountants – Business Card</title>
<link rel="stylesheet" href="https://fonts.googleapis.com/css2?family=Source+Sans+3:wght@400;600;700&display=swap">
<style>
  :root {
    --backdrop: #e9ebed;
    --card-white: #f7f8f9;
    --brand-blue: #1596cf;
    --brand-blue-deep: #0e86bf;
    --brand-blue-light: #2aaade;
    --accent-yellow: #f2c200;
    --watermark-white: rgba(3, 147, 206, 0.16);
    --watermark-blue: rgba(255, 255, 255, 0.16);
    --text-white: #ffffff;
    --text-white-soft: rgba(255, 255, 255, 0.88);
  }
  * { box-sizing: border-box; margin: 0; padding: 0; }
  html, body {
    width: 1200px;
    height: 800px;
    overflow: hidden;
    background: var(--backdrop);
    font-family: "Source Sans 3", "Helvetica Neue", Arial, sans-serif;
  }
  .canvas {
    position: relative;
    width: 1200px;
    height: 800px;
  }
  .card {
    position: absolute;
    top: 255px;
    width: 500px;
    height: 290px;
    overflow: hidden;
    border-radius: 3px;
    box-shadow: 0 10px 30px rgba(0, 0, 0, 0.12);
  }
  .card-front { left: 70px; background: var(--card-white); }
  .card-back {
    left: 630px;
    background: linear-gradient(160deg, var(--brand-blue-light), var(--brand-blue-deep));
    color: var(--text-white);
  }

  .watermark {
    position: absolute;
    border-radius: 50%;
  }
  .card-front .watermark {
    width: 300px; height: 300px;
    right: -70px; bottom: -110px;
    background: var(--watermark-white);
  }
  .card-back .watermark {
    width: 250px; height: 250px;
    right: -60px; bottom: -120px;
    background: var(--watermark-blue);
  }

  .wordmark {
    position: absolute;
    display: flex;
    align-items: center;
    gap: 10px;
    font-weight: 700;
    line-height: 1;
    white-space: nowrap;
  }
  .wordmark-square {
    width: 12px; height: 12px;
    background: var(--accent-yellow);
    flex: none;
  }
  .card-front .wordmark {
    left: 36px; top: 92px;
    font-size: 32px;
    color: var(--brand-blue);
  }
  .card-back .wordmark {
    left: 262px; top: 86px;
    font-size: 20px;
    color: var(--text-white);
    gap: 7px;
  }
  .card-back .wordmark-square { width: 8px; height: 8px; }

  .holder {
    position: absolute;
    left: 40px; top: 40px;
  }
  .holder-name { font-size: 21px; font-weight: 700; }
  .holder-title { font-size: 13px; font-weight: 600; margin-top: 2px; color: var(--text-white-soft); }
  .holder-address { font-size: 12px; margin-top: 10px; color: var(--text-white-soft); }

  .contact-list {
    position: absolute;
    list-style: none;
    font-size: 12px;
    color: var(--text-white-soft);
  }
  .contact-list li {
    display: flex;
    align-items: center;
    gap: 8px;
    margin-bottom: 6px;
  }
  .contact-icon {
    width: 14px; height: 14px;
    flex: none;
  }
  .contact-phone { left: 40px; top: 142px; }
  .contact-online { left: 232px; top: 190px; }
</style>
</head>
<body>
<main class="canvas">

  <section class="card card-front" aria-label="Business card front">
    <div class="watermark" aria-hidden="true"></div>
    <div class="wordmark">
      <span class="wordmark-square" aria-hidden="true"></span>
      <span>Wendrows Accountants</span>
    </div>
  </section>

  <section class="card card-back" aria-label="Business card back">
    <div class="watermark" aria-hidden="true"></div>

    <div class="holder">
      <p class="holder-name">Martin Osgood</p>
      <p class="holder-title">FCPA</p>
      <p class="holder-address">2718 Park Road Ashvale VIC 3199</p>
    </div>

    <ul class="contact-list contact-phone">
      <li>
        <svg class="contact-icon" viewBox="0 0 16 16" aria-hidden="true">
          <circle cx="8" cy="8" r="7.2" fill="none" stroke="#fff" stroke-width="1"/>
          <path d="M5.2 4.4l1.3-.3.8 1.8-.8.7c.4.9 1 1.6 1.9 2l.7-.8 1.8.8-.3 1.3c-2.9.2-5.6-2.6-5.4-5.5z" fill="#fff"/>
        </svg>
        <span>+61 3 94827713</span>
      </li>
      <li>
        <svg class="contact-icon" viewBox="0 0 16 16" aria-hidden="true">
          <circle cx="8" cy="8" r="7.2" fill="none" stroke="#fff" stroke-width="1"/>
          <rect x="5" y="4" width="6" height="3" fill="none" stroke="#fff" stroke-width="0.9"/>
          <rect x="4" y="7" width="8" height="4" rx="0.6" fill="#fff"/>
        </svg>
        <span>+ 61 9482 7159</span>
      </li>
    </ul>

    <div class="wordmark">
      <span class="wordmark-square" aria-hidden="true"></span>
      <span>Wendrows Accountants</span>
    </div>

    <ul class="contact-list contact-online">
      <li>
        <svg class="contact-icon" viewBox="0 0 16 16" aria-hidden="true">
          <circle cx="8" cy="8" r="7.2" fill="none" stroke="#fff" stroke-width="1"/>
          <rect x="4" y="5.2" width="8" height="5.6" fill="none" stroke="#fff" stroke-width="0.9"/>
          <path d="M4 5.4l4 3 4-3" fill="none" stroke="#fff" stroke-width="0.9"/>
        </svg>
        <span>martin@wendrows-example.com.au</span>
      </li>
      <li>
        <svg class="contact-icon" viewBox="0 0 16 16" aria-hidden="true">
          <circle cx="8" cy="8" r="7.2" fill="none" stroke="#fff" stroke-width="1"/>
          <circle cx="8" cy="8" r="3.6" fill="none" stroke="#fff" stroke-width="0.9"/>
          <path d="M4.4 8h7.2M8 4.4c-1.6 2.2-1.6 5 0 7.2M8 4.4c1.6 2.2 1.6 5 0 7.2" fill="none" stroke="#fff" stroke-width="0.8"/>
        </svg>
        <span>wendrowsaccountants-example.com.au</span>
      </li>
    </ul>
  </section>

</main>
</body>
</html>
```